Pennfield Hearing Clinic Business Card Design Project

We need a new business card design. We changed our logo recently and need to update our cards. We are a small hearing clinic with a 3 locations in BC. We help people with hearing loss by fitting them with hearing instruments that are appropriate for them and help them overcome the challenges that hearing loss causes. The symbol part of our logo represents the three important components of successful outcome. The three are: 1-acceptance of the change in hearing, 2-a hearing care provider that cares and is knowledgeable and experienced, 3-a quality hearing instrument. I would like to have a clean design that shows quality commitment to a successful end result of treatment. Here is our website for more information. www.sonvale.ca

Target Market(s)

Senior population - mostly 50+

Industry/Entity Type

Clinic

Requirements
Must have
• Logo
Name - Derek Olsbrand
Title - Hearing Instrument Practitioner (can be very small)
Phone: 250 637-5814
Address: 415-B 22nd Street, Harlow Creek, BC V2X 7K3
Email: derek@sonvale.ca
website address: www.sonvale.ca
Nice to have
• Could be both sided and have a photo on the card.

```html
<!DOCTYPE html>
<html lang="en">
<head>
<meta charset="utf-8">
<title>Pennfield Hearing Clinic – Business Cards</title>
<link rel="stylesheet" href="https://fonts.googleapis.com/css2?family=Ubuntu:wght@400;500;700&display=swap">
<style>
  :root {
    --stage: #1f1f1f;
    --orange: #f39222;
    --green: #9acb3c;
    --blue: #235ead;
    --paper: #ffffff;
    --ink-blue: #2a57a8;
    --ink-orange: #f08c1e;
    --ink-green: #8cc63f;
  }
  * { margin: 0; padding: 0; box-sizing: border-box; }
  html, body { width: 1200px; height: 900px; overflow: hidden; }
  body {
    background: var(--stage);
    font-family: "Ubuntu", Arial, sans-serif;
    position: relative;
  }
  .card {
    position: absolute;
    width: 420px;
    height: 236px;
  }
  .card--orange { left: 165px; top: 200px; background: var(--orange); }
  .card--green  { left: 616px; top: 200px; background: var(--green); }
  .card--blue   { left: 164px; top: 465px; background: var(--blue); }
  .card--contact { left: 618px; top: 465px; background: var(--paper); }

  .brand {
    position: absolute;
    right: 35px;
    top: 157px;
    display: flex;
    align-items: center;
    gap: 7px;
    color: var(--paper);
    font-weight: 700;
    font-size: 20px;
    letter-spacing: -0.3px;
    white-space: nowrap;
  }
  .brand__dot {
    width: 17px; height: 17px;
    border-radius: 50%;
    background: currentColor;
  }
  .website {
    position: absolute;
    right: 35px;
    top: 196px;
    color: var(--paper);
    font-size: 13px;
    letter-spacing: 0.2px;
  }

  .card--contact .brand {
    top: 63px;
    right: 42px;
    color: var(--ink-blue);
  }
  .contact {
    position: absolute;
    right: 40px;
    top: 140px;
    text-align: right;
    color: var(--ink-blue);
    font-size: 9.5px;
    line-height: 1;
  }
  .contact__name {
    color: var(--ink-orange);
    font-weight: 700;
    font-size: 14px;
    margin-bottom: 4px;
  }
  .contact__title { margin-bottom: 10px; }
  .contact__address { margin-bottom: 9px; }
  .contact__label { color: var(--ink-green); }
  .contact__gap { display: inline-block; width: 5px; }
</style>
</head>
<body>
  <section class="card card--orange">
    <div class="brand"><span class="brand__dot"></span>Pennfield Hearing Clinic</div>
    <div class="website">www.sonvale.ca</div>
  </section>

  <section class="card card--green">
    <div class="brand"><span class="brand__dot"></span>Pennfield Hearing Clinic</div>
    <div class="website">www.sonvale.ca</div>
  </section>

  <section class="card card--blue">
    <div class="brand"><span class="brand__dot"></span>Pennfield Hearing Clinic</div>
    <div class="website">www.sonvale.ca</div>
  </section>

  <section class="card card--contact">
    <div class="brand"><span class="brand__dot"></span>Pennfield Hearing Clinic</div>
    <div class="contact">
      <p class="contact__name">Derek Olsbrand</p>
      <p class="contact__title">Hearing Instrument Practitioner</p>
      <p class="contact__address">415-B 22nd Street, Harlow Creek, BC V2X 7K3</p>
      <p class="contact__lines">
        <span class="contact__label">Phone:</span> 250 637-5814<span class="contact__gap"></span>
        <span class="contact__label">Email:</span> derek@sonvale.ca
      </p>
    </div>
  </section>
</body>
</html>
```